Unique Elegant Stationary Set

Prepare a unique eye catching stationary set consisting of :
(1) Letterhead
(2) A3 Envelope
(3) Business Card
(4) Email Signature Banner

Package to be elegant, modern, and designers not only to think of design or colors but also materials could make a big difference, embossing, debossing, glossy, matt ....etc.

I attached both our new logos (Stacked or Linear) noting you may use any of them but you cant modify anything in the logos. Also attached our final draft portfolio to see what type of projects we work on and i also have here a glimmerboard page link showing the direction we want: https://www.glimmerboard.example/dorvanmelik/business-card-design/

Target Market(s)

VVIP / Elite Developers

Industry/Entity Type

Architecture

Font styles to use
Sans Serif
Other font styles liked:
• unitext

Requirements
Should not have
• too many colors, or being busy in general. We want something pleasing to the eye

```html
<!DOCTYPE html>
<html lang="en">
<head>
<meta charset="utf-8">
<title>Kavro Studio – Stationery Set</title>
<link rel="stylesheet" href="https://fonts.googleapis.com/css2?family=Lato:wght@400;700;900&display=swap">
<style>
:root{
  --red:#c0202b;
  --ink:#222222;
  --paper:#ffffff;
  --canvas:#dcdcdc;
  --black-card:#1c1c1c;
  --deboss:#101010;
  --gold:#c08a3a;
  --faint:#e4e4e4;
  --rule:#9a9a9a;
}
*{margin:0;padding:0;box-sizing:border-box}
html,body{width:1200px;height:884px;overflow:hidden}
body{background:var(--canvas);font-family:'Lato',sans-serif;color:var(--ink);position:relative}
.piece{position:absolute;background:var(--paper);box-shadow:0 2px 8px rgba(0,0,0,.12)}
.wordmark{font-weight:900;color:var(--red);letter-spacing:.04em;line-height:1;white-space:nowrap;display:flex;align-items:center;gap:6px}
.wordmark .mark{display:inline-block;background:currentColor}
.contact{list-style:none;font-size:8px;line-height:1.7;text-transform:uppercase}
.contact li{display:flex;align-items:center;gap:5px}
.contact svg{width:9px;height:9px;flex:none}

/* business cards */
.card{width:220px;height:126px;border-radius:4px}
.card-white-front{left:30px;top:30px;display:flex;flex-direction:column;align-items:center;justify-content:center;gap:10px}
.card-white-front .wordmark{font-size:22px}
.card-white-front .mark{width:10px;height:10px}
.card-web{font-size:8px;letter-spacing:.04em}
.card-back{padding:16px 16px}
.card-white-back{left:260px;top:30px}
.card-name{font-size:10px;font-weight:700;color:var(--red);text-transform:uppercase}
.card-role{font-size:7px;text-transform:uppercase;margin-bottom:10px}
.card-back .contact{font-size:7px;line-height:1.6}
.card-back .wordmark{position:absolute;left:16px;bottom:12px;font-size:11px}
.card-back .mark{width:6px;height:6px}
.card-black{background:var(--black-card);border-radius:8px}
.card-black-front{left:490px;top:30px;display:flex;flex-direction:column;align-items:center;justify-content:center;gap:10px}
.card-black-front .wordmark{color:var(--deboss);font-size:22px}
.card-black-front .mark{width:10px;height:10px}
.card-black-front .card-web{color:var(--deboss)}
.card-black-back{left:720px;top:30px;color:var(--gold)}
.card-black-back .card-name,.card-black-back .wordmark{color:var(--gold)}

/* letterhead */
.letterhead{left:30px;top:186px;width:460px;height:650px;padding:34px 36px;overflow:hidden}
.lh-header{display:flex;align-items:flex-end;gap:10px}
.lh-header .wordmark{font-size:18px}
.lh-header .mark{width:8px;height:8px}
.lh-rule{flex:1;height:1px;background:var(--red);margin-bottom:6px}
.lh-address{font-size:6px;text-align:right;line-height:1.5;text-transform:uppercase}
.lh-address em{font-style:normal;color:var(--red)}
.lh-body{margin-top:34px;font-size:8.5px;line-height:1.95;font-weight:700}
.lh-body p{margin-bottom:8px}
.lh-sign{margin-top:18px;font-size:8.5px;font-weight:700;line-height:1.9}
.signature{width:90px;height:22px;background:linear-gradient(90deg,#eeeeee,#d4d4d4);margin:4px 0}
.watermark{position:absolute;left:36px;bottom:22px;font-weight:900;font-size:64px;color:var(--faint);letter-spacing:.02em;white-space:nowrap}

/* envelope */
.envelope-back{left:520px;top:186px;width:270px;height:430px;overflow:hidden}
.flap{height:46px;background:linear-gradient(180deg,#a30f19,var(--red));border-radius:0 0 10px 10px}
.envelope-front{left:640px;top:256px;width:300px;height:580px;overflow:hidden}
.envelope-front .wordmark{position:absolute;right:20px;top:22px;font-size:18px}
.envelope-front .mark{width:8px;height:8px}
.env-footer{position:absolute;left:0;right:0;bottom:0;height:64px}
.env-band{position:absolute;right:0;bottom:34px;width:190px;height:8px;background:var(--red)}
.env-info{position:absolute;left:112px;bottom:44px;font-size:5.5px;line-height:1.5;text-transform:uppercase}
.env-info strong{color:var(--red)}
.env-watermark{position:absolute;left:-2px;bottom:6px;font-weight:900;font-size:26px;color:var(--faint);white-space:nowrap}

/* email signature */
.email-signature{left:970px;top:250px;width:208px;height:300px;padding:18px 16px;box-shadow:none}
.email-signature .contact{font-size:8.5px;line-height:2;text-transform:none}
.email-signature .contact svg{width:10px;height:10px}
.es-address{font-size:8.5px;line-height:1.3;margin:2px 0 12px;text-transform:uppercase}
.es-address em{font-style:normal;color:var(--red)}
.email-signature .wordmark{font-size:22px}
.email-signature .mark{width:10px;height:10px}
.es-rule{height:1px;background:var(--ink);margin:10px 0 8px}
.es-disclaimer{font-size:7.6px;line-height:1.35}
</style>
</head>
<body>

<svg width="0" height="0" style="position:absolute" aria-hidden="true">
  <defs>
    <symbol id="icon-phone" viewBox="0 0 12 12"><circle cx="6" cy="6" r="5.3" fill="none" stroke="currentColor"/><path d="M4 3.3l1 1.2-.6.8c.4.8 1 1.4 1.8 1.8l.8-.6 1.2 1-.6 1c-2 0-4.3-2.3-4.3-4.3z" fill="currentColor"/></symbol>
    <symbol id="icon-mail" viewBox="0 0 12 12"><circle cx="6" cy="6" r="5.3" fill="none" stroke="currentColor"/><rect x="3.3" y="4" width="5.4" height="4" fill="none" stroke="currentColor" stroke-width=".8"/><path d="M3.3 4l2.7 2.2L8.7 4" fill="none" stroke="currentColor" stroke-width=".8"/></symbol>
    <symbol id="icon-web" viewBox="0 0 12 12"><circle cx="6" cy="6" r="5.3" fill="none" stroke="currentColor"/><circle cx="6" cy="6" r="3" fill="none" stroke="currentColor" stroke-width=".7"/><path d="M3 6h6M6 3v6" stroke="currentColor" stroke-width=".7"/></symbol>
  </defs>
</svg>

<!-- business card, white, front -->
<section class="piece card card-white-front">
  <div class="wordmark"><span class="mark"></span>KAVRO STUDIO</div>
  <div class="card-web">WWW.KAVROSTUDIO.EXAMPLE</div>
</section>

<!-- business card, white, back -->
<section class="piece card card-back card-white-back">
  <div class="card-name">Rami Name</div>
  <div class="card-role">Designation</div>
  <ul class="contact">
    <li><svg style="color:var(--red)"><use href="#icon-phone"/></svg>+971 2 555 0142</li>
    <li><svg style="color:var(--red)"><use href="#icon-mail"/></svg>info@kavrostudio.example</li>
    <li><svg style="color:var(--red)"><use href="#icon-web"/></svg>www.kavrostudio.example</li>
    <li>Meridian Tower, 14th Floor, 1405</li>
    <li>P.O. Box: 50211</li>
  </ul>
  <div class="wordmark"><span class="mark"></span>KAVRO STUDIO</div>
</section>

<!-- business card, black, front -->
<section class="piece card card-black card-black-front">
  <div class="wordmark"><span class="mark"></span>KAVRO STUDIO</div>
  <div class="card-web">WWW.KAVROSTUDIO.EXAMPLE</div>
</section>

<!-- business card, black, back -->
<section class="piece card card-back card-black card-black-back">
  <div class="card-name">Rami Name</div>
  <div class="card-role">Designation</div>
  <ul class="contact">
    <li><svg><use href="#icon-phone"/></svg>+971 2 555 0142</li>
    <li><svg><use href="#icon-mail"/></svg>info@kavrostudio.example</li>
    <li><svg><use href="#icon-web"/></svg>www.kavrostudio.example</li>
    <li>Meridian Tower, 14th Floor, 1405</li>
    <li>P.O. Box: 50211</li>
  </ul>
  <div class="wordmark"><span class="mark"></span>KAVRO STUDIO</div>
</section>

<!-- letterhead -->
<section class="piece letterhead">
  <header class="lh-header">
    <div class="wordmark"><span class="mark"></span>KAVRO STUDIO</div>
    <div class="lh-rule"></div>
    <div class="lh-address"><em>Meridian Tower,</em> 14th Floor, 1405, P.O. Box: 50211<br>+971 2 555 0142 &nbsp; info@kavrostudio.example</div>
  </header>
  <div class="lh-body">
    <p>Lorem ipsum dolor sit amet,<br>consectetuer adipiscing elit, sed diam nonummy nibh euismod tincidunt ut laoreet dolore magna aliquam erat volutpat. Ut wisi enim ad minim veniam, quis nostrud exerci tation ullamcorper suscipit lobortis nisl ut aliquip ex ea commodo consequat. Duis autem vel eum iriure dolor in hendrerit in vulputate velit esse molestie consequat, vel illum dolore eu feugiat nulla facilisis at vero eros et accumsan et iusto odio dignissim qui blandit praesent luptatum zzril delenit augue duis dolore te feugait nulla facilisi.</p>
    <p>Lorem ipsum dolor sit amet, cons ectetuer adipiscing elit, sed diam nonummy nibh euismod tincidunt ut laoreet dolore magna aliquam erat volutpat. Ut wisi enim ad minim veniam, quis nostrud exerci tation ullamcorper suscipit lobortis nisl ut aliquip ex ea commodo consequat. Duis autem vel eum iriure dolor in hendrerit in vulputate velit esse molestie consequat, vel illum dolore eu feugiat nulla facilisis at vero eros et accumsan et iusto odio dignissim qui blandit praesent luptatum zzril delenit augue.</p>
  </div>
  <div class="lh-sign">
    duis dolore te feugait nulla facilisi.
    <div class="signature" role="img" aria-label="Handwritten signature"></div>
    Lorem ipsum<br>dolor sit amet,
  </div>
  <div class="watermark" aria-hidden="true">KAVRO STUDIO</div>
</section>

<!-- A3 envelope, back with flap -->
<section class="piece envelope-back">
  <div class="flap"></div>
</section>

<!-- A3 envelope, front -->
<section class="piece envelope-front">
  <div class="wordmark"><span class="mark"></span>KAVRO STUDIO</div>
  <div class="env-footer">
    <div class="env-info"><strong>Kavro Studio</strong><br>Meridian Tower, 14th Floor, 1405, P.O. Box 50211<br>+971 2 555 0142 &nbsp; info@kavrostudio.example</div>
    <div class="env-band"></div>
    <div class="env-watermark" aria-hidden="true">KAVRO STUDIO</div>
  </div>
</section>

<!-- email signature -->
<section class="piece email-signature">
  <ul class="contact">
    <li><svg style="color:var(--red)"><use href="#icon-phone"/></svg>+971 2 555 0142</li>
    <li><svg style="color:var(--red)"><use href="#icon-mail"/></svg>INFO@KAVROSTUDIO.EXAMPLE</li>
    <li><svg style="color:var(--red)"><use href="#icon-web"/></svg>WWW.KAVROSTUDIO.EXAMPLE</li>
  </ul>
  <div class="es-address"><em>Meridian Tower,</em> 14th Floor, 1405,<br>P.O. Box: 50211</div>
  <div class="wordmark"><span class="mark"></span>KAVRO STUDIO</div>
  <div class="es-rule"></div>
  <p class="es-disclaimer">KAVRO STUDIO accepts no liability for the content of this email, or for the consequences of any actions taken on the basis of the information provided, unless that information is subsequently confirmed in writing. If you are not the intended recipient you are notified that disclosing, copying, distributing or taking any action in reliance on the contents of this information is strictly prohibited.</p>
</section>

</body>
</html>
```